SOC audit and security advisory company

We are a small public accounting firm that specializes in SOC attestations for small to medium sized business throughout the U.S. Our business is much like consulting, but we form an opinion about their operational controls. We are looking for "relevance and with a hint of polished sophistication". Our logo colors are dark gray and red. Our existing site is www.tolvanpartners.com for detailed information. We would like to include some type of captcha if possible. This is an information only site.

Target Market(s)

Small to medium sized financial and IT audit companies that are innovative and flexible.

Industry/Entity Type

Auditing

Coding

Coded - Design and coding required

Number of Pages Required

4 page

Font styles to use
Sans Serif

Requirements
Must have
• Good flow and attention to the content.
Nice to have
• CAPTCHA for contact us page
Should not have
• Big Bold lines.
• Too many distractions.

```html
<!DOCTYPE html>
<html lang="en">
<head>
<meta charset="utf-8">
<title>Tolvan Audit &amp; Advisory</title>
<link href="https://fonts.googleapis.com/css2?family=Roboto:wght@300;400;500&display=swap" rel="stylesheet">
<style>
:root{
  --red:#c9291f;
  --ink:#3d3d3d;
  --text:#4a4a4a;
  --band:#f4f4f4;
  --footer:#1f1f1f;
  --footer-bottom:#121212;
  --footer-text:#d6d6d6;
  --white:#fff;
}
*{box-sizing:border-box;margin:0;padding:0}
html,body{width:1200px;height:2320px;overflow:hidden}
body{position:relative;background:var(--white);font-family:'Roboto',Arial,sans-serif;color:var(--text)}

/* header */
.site-header{position:absolute;left:0;top:0;width:1200px;height:127px;background:var(--white)}
.brand{position:absolute;left:100px;top:22px;display:flex;align-items:center;gap:12px}
.brand-dot{width:26px;height:26px;border-radius:50%;background:var(--red)}
.brand-name{font-size:44px;font-weight:400;color:var(--ink);letter-spacing:1px}
.main-nav a{position:absolute;top:53px;font-size:14px;color:#555;text-decoration:none;white-space:nowrap}
.main-nav a.active{color:var(--red)}
.nav-underline{position:absolute;left:497px;top:80px;width:32px;height:2px;background:var(--red)}
.search-icon{position:absolute;left:1084px;top:55px}

/* hero */
.hero{position:absolute;left:0;top:127px;width:1200px;height:541px;
  background:linear-gradient(100deg,#5a4636 0%,#a88a6c 35%,#c9b49a 55%,#6b6a6c 80%,#2f3440 100%)}
.hero-title{position:absolute;left:688px;top:290px;font-size:56px;font-weight:300;color:var(--white)}
.hero-text{position:absolute;left:690px;top:364px;width:420px;font-size:16px;line-height:25px;color:var(--white)}
.hero-arrow{position:absolute;top:230px}

/* section headings */
.section-title{position:absolute;left:0;width:1200px;text-align:center;font-size:35px;font-weight:400;color:var(--ink);letter-spacing:.5px}
.section-title span,.company-title span{color:var(--red)}
.rule{position:absolute;width:36px;height:2px;background:var(--red)}

/* why */
.why-intro{position:absolute;left:0;top:780px;width:1200px;text-align:center;font-size:12.5px;color:#444}
.feature-icon{position:absolute;width:116px;height:116px;border-radius:50%;background:#f0f0f0;border:1px solid #e4e4e4;display:flex;align-items:center;justify-content:center}
.feature-icon.highlight{background:var(--red);border-color:var(--red)}
.feature-label{position:absolute;top:943px;width:240px;text-align:center;font-size:17px;font-weight:500;color:#555}
.feature-label.highlight{color:var(--red)}

/* services */
.services{position:absolute;left:0;top:1016px;width:1200px;height:527px;background:var(--band)}
.service-photo{position:absolute;top:1132px;width:322px;height:244px;border:1px solid #ddd}
.service-title{position:absolute;top:1404px;font-size:17px;font-weight:500;color:var(--red);white-space:nowrap}
.service-text{position:absolute;top:1439px;width:322px;font-size:12.5px;line-height:23px;color:#555;text-align:justify}

/* company */
.company-photo{position:absolute;left:131px;top:1609px;width:407px;height:330px;
  background:linear-gradient(135deg,#2e3442 0%,#6a7282 40%,#d9e2ee 70%,#f4f6fa 100%)}
.company-title{position:absolute;left:566px;top:1600px;font-size:35px;font-weight:400;color:var(--ink)}
.company-text{position:absolute;left:568px;top:1684px;width:504px;font-size:12.5px;line-height:22.5px;color:#555;text-align:justify}
.btn-read{position:absolute;left:569px;top:1888px;width:108px;height:44px;background:var(--red);color:var(--white);font-size:15px;display:flex;align-items:center;justify-content:center;border-radius:2px}

/* footer */
.site-footer{position:absolute;left:0;top:2004px;width:1200px;height:267px;background:var(--footer);color:var(--footer-text)}
.footer-brand{position:absolute;left:110px;top:38px;display:flex;align-items:center;gap:9px}
.footer-brand .brand-dot{width:18px;height:18px}
.footer-brand .brand-name{font-size:30px;color:#bdbdbd}
.footer-about{position:absolute;left:110px;top:90px;width:190px;font-size:12.5px;line-height:22px;text-align:justify}
.footer-contact{position:absolute;left:110px;font-size:12px;display:flex;align-items:center;gap:14px}
.social{position:absolute;top:2226px;width:24px;height:24px;border-radius:50%;background:var(--red)}
.footer-heading{position:absolute;top:46px;font-size:15px;font-weight:500;color:var(--white)}
.footer-list{position:absolute;left:382px;top:89px;list-style:none;font-size:12.5px;line-height:22px}
.footer-list li{display:flex;align-items:center;gap:8px}
.footer-list li::before{content:"";width:7px;height:7px;border:2px solid var(--red);border-radius:50%}
.tweets{position:absolute;left:574px;top:92px;width:242px;font-size:12.5px;line-height:26px;text-align:justify}
.tweets .tweet-body{text-indent:18px}
.tweets .time{color:var(--red)}
.signup-text{position:absolute;left:881px;top:84px;width:220px;font-size:11.5px;line-height:19px}
.field{position:absolute;left:881px;width:217px;height:43px;border:1px solid #555;border-radius:3px;background:#1a1a1a;font-size:11.5px;color:#ddd;padding:13px 15px}
.btn-subscribe{position:absolute;left:1000px;top:185px;width:98px;height:43px;background:var(--red);color:var(--white);font-size:12px;display:flex;align-items:center;justify-content:center;border-radius:0 3px 3px 0}
.copyright{position:absolute;left:0;top:2271px;width:1200px;height:49px;background:var(--footer-bottom);color:#eee;font-size:12.5px;text-align:center;line-height:49px}
</style>
</head>
<body>

<header class="site-header">
  <div class="brand"><span class="brand-dot"></span><span class="brand-name">TOLVAN</span></div>
  <nav class="main-nav">
    <a class="active" style="left:496px">Home</a>
    <a style="left:596px">SOC and Advisory Services</a>
    <a style="left:830px">About Us</a>
    <a style="left:950px">Contact Us</a>
  </nav>
  <span class="nav-underline"></span>
  <svg class="search-icon" width="18" height="18" viewBox="0 0 18 18" aria-hidden="true">
    <circle cx="7.5" cy="7.5" r="5.5" fill="none" stroke="var(--red)" stroke-width="2.5"/>
    <path d="M11.5 11.5 L16 16" stroke="var(--red)" stroke-width="2.8" stroke-linecap="round"/>
  </svg>
</header>

<section class="hero" role="img" aria-label="Photo of a hand writing with a pen over financial documents and a laptop">
  <svg class="hero-arrow" style="left:38px" width="16" height="72" viewBox="0 0 16 72" aria-hidden="true"><path d="M14 2 L3 36 L14 70" fill="none" stroke="#fff" stroke-width="1.5"/></svg>
  <svg class="hero-arrow" style="left:1143px" width="16" height="72" viewBox="0 0 16 72" aria-hidden="true"><path d="M2 2 L13 36 L2 70" fill="none" stroke="#fff" stroke-width="1.5"/></svg>
  <h1 class="hero-title">Who We Are</h1>
  <p class="hero-text">Our team is made up of seasoned professionals with back-grounds in regulatory compliance, IT audit, financial audit, and IT professional services.</p>
</section>

<h2 class="section-title" style="top:712px">WHY <span>TOLVAN?</span></h2>
<span class="rule" style="left:582px;top:768px"></span>
<p class="why-intro">Our proven implementation and audit models allow for capturing requirements while expiditing the process.</p>

<div class="feature-icon" style="left:247px;top:812px">
  <svg width="44" height="44" viewBox="0 0 44 44" aria-hidden="true">
    <circle cx="28" cy="16" r="10" fill="#4a4a4a"/>
    <path d="M21 23 L7 37" stroke="#4a4a4a" stroke-width="6" stroke-linecap="round"/>
  </svg>
</div>
<div class="feature-icon highlight" style="left:542px;top:812px">
  <svg width="54" height="54" viewBox="0 0 54 54" aria-hidden="true" fill="none" stroke="#fff" stroke-width="2">
    <circle cx="18" cy="18" r="11"/>
    <path d="M13 23 L23 13"/><circle cx="14" cy="14" r="1.5"/><circle cx="22" cy="22" r="1.5"/>
    <rect x="26" y="30" width="22" height="18"/>
    <path d="M31 35h4M39 35h4M31 41h4M39 41h4M30 30V24h6v6"/>
  </svg>
</div>
<div class="feature-icon" style="left:837px;top:812px">
  <svg width="44" height="48" viewBox="0 0 44 48" aria-hidden="true" fill="none" stroke="#4a4a4a" stroke-width="2">
    <rect x="6" y="6" width="32" height="38" rx="2"/>
    <rect x="15" y="2" width="14" height="7" rx="1"/>
    <path d="M11 26 h5 l3 -7 l4 12 l3 -5 h7"/>
  </svg>
</div>
<p class="feature-label" style="left:185px">Free Consultations</p>
<p class="feature-label highlight" style="left:480px">Fixed Cost</p>
<p class="feature-label" style="left:775px">Results driven</p>

<section class="services">
  <h2 class="section-title" style="top:24px">SOC AND <span>ADVISORY SERVICES</span></h2>
  <span class="rule" style="left:582px;top:84px"></span>
</section>

<div class="service-photo" style="left:97px;background:linear-gradient(135deg,#7d8fa3 0%,#dfe6ee 45%,#f7f8fa 100%)" role="img" aria-label="Photo of a hand signing a financial report with a pen"></div>
<div class="service-photo" style="left:439px;background:radial-gradient(circle at 50% 50%,#e9f4f7 0%,#7ba9b8 45%,#2c4f5f 100%)" role="img" aria-label="Digital security illustration with a red padlock over circuitry"></div>
<div class="service-photo" style="left:779px;background:linear-gradient(135deg,#c9ccd0 0%,#eef0f2 50%,#ffffff 100%)" role="img" aria-label="Photo of hands holding a smartphone beside a laptop"></div>

<h3 class="service-title" style="left:97px">Consumer Financial Compliance Reviews</h3>
<h3 class="service-title" style="left:439px">HIPAA Security Assessments</h3>
<h3 class="service-title" style="left:779px">IT Security Reviews</h3>
<p class="service-text" style="left:97px">As a result of Wall Street reform, companies who are consumer facing must meet a minimum federally regulated posture in business...</p>
<p class="service-text" style="left:439px">Our staff of certified HIPAA professionals can help to identify and close those gaps that pose threats to your business model...</p>
<p class="service-text" style="left:779px">A "perimeter in" review is conducted based on CORA, CoVET, ISARA and IQS frameworks. Our staff consists of certified professionals to assist your team in ensuring the best approach to securing your IT infrastructure.</p>

<div class="company-photo" role="img" aria-label="Photo of a business team reviewing charts and documents at a desk"></div>
<h2 class="company-title">OUR <span>COMPANY</span></h2>
<span class="rule" style="left:668px;top:1660px"></span>
<p class="company-text">Tolvan was founded to put the consultation back into audit and professional services. We were founded on the belief that merely performing a services does not constitute building relationships. With that in mind, we take a unique approach to engaging our clients so they can get the most out of their experience with Tolvan. Tolvan was established to provide boutique audit and advisoy services to small to medium sized businesses.<br>We know that every company is different. We take a consultitive approach to engaging our clients so they fully understand the process and get something more than just a report! Our clients gain knowledge!</p>
<div class="btn-read">Read More</div>

<footer class="site-footer">
  <div class="footer-brand"><span class="brand-dot"></span><span class="brand-name">TOLVAN</span></div>
  <p class="footer-about">Tolvan was founded to put the consultation back into audit and professional services.</p>
  <div class="footer-contact" style="top:172px">
    <svg width="13" height="13" viewBox="0 0 24 24" aria-hidden="true"><path fill="#fff" d="M6.6 10.8c1.4 2.8 3.8 5.1 6.6 6.6l2.2-2.2c.3-.3.7-.4 1-.2 1.1.4 2.3.6 3.6.6.6 0 1 .4 1 1V20c0 .6-.4 1-1 1C10.6 21 3 13.4 3 4c0-.6.4-1 1-1h3.5c.6 0 1 .4 1 1 0 1.3.2 2.5.6 3.6.1.3 0 .7-.2 1z"/></svg>
    <span>1800 - 555 - 0142</span>
  </div>
  <div class="footer-contact" style="top:196px;left:133px">contact@tolvanpartners.com</div>

  <h4 class="footer-heading" style="left:382px">Our Services</h4>
  <ul class="footer-list">
    <li>IT audit</li>
    <li>financial audit</li>
    <li>IT professional services</li>
  </ul>

  <h4 class="footer-heading" style="left:574px">Recent Tweets</h4>
  <div class="tweets">
    <p>Contrary to popular belief</p>
    <p class="tweet-body">Lorem Ipsum is simply dummy text of the printing and typesetting industry. Lorem Ipsum has been the industry's standard dummy text ever since the 1500s.</p>
    <p class="time">2 hours ago</p>
  </div>

  <h4 class="footer-heading" style="left:881px;top:49px">Sign up a receive email</h4>
  <p class="signup-text">Excepteur sint occaecat cupidatat non proident, sunt in culpa qui</p>
  <div class="field" style="top:133px">Enter Name</div>
  <div class="field" style="top:185px">Enter Email</div>
  <div class="btn-subscribe">SUBSCRIBE</div>
</footer>
<span class="social" style="left:130px"></span>
<span class="social" style="left:166px"></span>
<span class="social" style="left:200px"></span>

<div class="copyright">Copyright © 2016, Tolvan | All Rights Reserved.</div>

</body>
</html>
```